Corvane spray foam and Environmental

I have business cards but need new ones. The ones I have are very bland. Here is. Y company website http://www.corvanesprayfoam.ca

Also I can send you copies of the current cards
I would also need my current logo on the new design as well.. Also spray foam and Environmental

Industry/Entity Type

Business

Logo Text

Corvane.

```html
<!DOCTYPE html>
<html lang="en">
<head>
<meta charset="utf-8">
<title>Corvane Business Cards</title>
<link href="https://fonts.googleapis.com/css2?family=Open+Sans:wght@400;700;800&family=Roboto+Condensed:wght@400;700&display=swap" rel="stylesheet">
<style>
  :root {
    --purple: #6b3a80;
    --white: #ffffff;
    --backdrop: #d9d9d9;
    --mark: #8a7d92;
  }
  * { box-sizing: border-box; margin: 0; padding: 0; }
  html, body { width: 1200px; height: 1000px; overflow: hidden; }
  body { background: var(--backdrop); position: relative; font-family: "Open Sans", sans-serif; }

  .card {
    position: absolute;
    background: var(--white);
    border-radius: 34px;
    overflow: hidden;
  }
  .card--front { left: 150px; top: 102px; width: 630px; height: 358px; }
  .card--back  { left: 370px; top: 546px; width: 636px; height: 362px; }

  .brand { position: absolute; text-align: center; }
  .brand__square { background: var(--mark); border-radius: 8px; margin: 0 auto; }
  .brand__name {
    font-family: "Open Sans", sans-serif;
    font-weight: 800;
    color: var(--purple);
    letter-spacing: 0;
    line-height: 1;
    white-space: nowrap;
  }
  .card--front .brand { left: 25px; top: 99px; width: 276px; }
  .card--front .brand__square { width: 112px; height: 99px; }
  .card--front .brand__name { font-size: 46px; margin-top: 10px; }
  .card--back .brand { left: 40px; top: 104px; width: 254px; }
  .card--back .brand__square { width: 100px; height: 86px; }
  .card--back .brand__name { font-size: 41px; margin-top: 22px; }

  /* Front: services panel */
  .services {
    position: absolute; left: 313px; top: 0; right: 0; bottom: 0;
    background: var(--purple); color: var(--white);
  }
  .services__heading {
    position: absolute; left: 64px;
    font-family: "Roboto Condensed", sans-serif; font-weight: 700;
    font-size: 18px; letter-spacing: 0.3px;
  }
  .services__list {
    position: absolute; left: 82px; list-style: none;
    font-family: "Open Sans", sans-serif; font-size: 15px; line-height: 20.3px;
    letter-spacing: 0.2px;
  }
  .services__divider {
    position: absolute; left: 37px; width: 257px; top: 179px; height: 2px; background: var(--white);
  }

  /* Back: contacts */
  .contacts__rule {
    position: absolute; left: 316px; top: 0; bottom: 0; width: 3px; background: var(--purple);
  }
  .division__label {
    position: absolute; left: 333px;
    font-family: "Roboto Condensed", sans-serif; font-weight: 700;
    font-size: 23px; color: var(--purple);
  }
  .division__band {
    position: absolute; left: 319px; right: 0; background: var(--purple); color: var(--white);
  }
  .contact { position: absolute; display: flex; align-items: center; }
  .contact svg { flex: none; }
  .contact--phone {
    left: 37px;
    font-family: "Roboto Condensed", sans-serif; font-weight: 700; font-size: 28px;
  }
  .contact--phone svg { margin-right: 8px; }
  .contact--line { left: 44px; font-size: 15px; }
  .contact--line svg { margin-right: 13px; }
</style>
</head>
<body>

<section class="card card--front">
  <div class="brand">
    <div class="brand__square"></div>
    <div class="brand__name">CORVANE</div>
  </div>

  <div class="services">
    <h2 class="services__heading" style="top:20px;">SPRAY FOAM</h2>
    <ul class="services__list" style="top:48px;">
      <li>- ROOFING FOAM</li>
      <li>- SLABJACKING</li>
      <li>- 2POUND/HALF POUND</li>
      <li>- SOUND PROOFING</li>
      <li>- BATT INSULATION</li>
      <li>- ATTIC BLOW IN</li>
    </ul>
    <div class="services__divider"></div>
    <h2 class="services__heading" style="top:191px;">ENVIRONMENTAL</h2>
    <ul class="services__list" style="top:219px;">
      <li>- AIR MONITORING</li>
      <li>- ASBESTOS TESTING</li>
      <li>- ASBESTOS REMOVAL</li>
      <li>- BUIDING DEMOLITION</li>
      <li>- LEAD TESTING</li>
      <li>- MOULD REMOVAL</li>
    </ul>
  </div>
</section>

<section class="card card--back">
  <div class="brand">
    <div class="brand__square"></div>
    <div class="brand__name">CORVANE</div>
  </div>

  <div class="contacts__rule"></div>

  <h2 class="division__label" style="top:25px;">PRAYFOAM</h2>
  <div class="division__band" style="top:58px; height:120px;">
    <div class="contact contact--phone" style="top:11px;">
      <svg width="24" height="24" viewBox="0 0 24 24"><path fill="#fff" d="M6.6 10.8a15.2 15.2 0 0 0 6.6 6.6l2.2-2.2a1 1 0 0 1 1-.25 11.4 11.4 0 0 0 3.6.57 1 1 0 0 1 1 1V20a1 1 0 0 1-1 1A17 17 0 0 1 3 4a1 1 0 0 1 1-1h3.5a1 1 0 0 1 1 1c0 1.25.2 2.45.57 3.57a1 1 0 0 1-.25 1z"/></svg>
      <span>604-555-0142</span>
    </div>
    <div class="contact contact--line" style="top:52px;">
      <svg width="13" height="10" viewBox="0 0 13 10"><rect width="13" height="10" fill="#fff"/><path d="M0 0l6.5 5L13 0" stroke="#6b3a80" stroke-width="1.3" fill="none"/></svg>
      <span>corvanefoam@example.com</span>
    </div>
    <div class="contact contact--line" style="top:82px;">
      <svg width="13" height="13" viewBox="0 0 14 14"><circle cx="7" cy="7" r="6" fill="none" stroke="#fff" stroke-width="1.4"/><path d="M1 7h12M7 1c-3 3.5-3 8.5 0 12M7 1c3 3.5 3 8.5 0 12" stroke="#fff" stroke-width="1.2" fill="none"/></svg>
      <span>www.corvanesprayfoam.ca</span>
    </div>
  </div>

  <h2 class="division__label" style="top:182px;">ENVIRONMENTAL</h2>
  <div class="division__band" style="top:212px; height:126px;">
    <div class="contact contact--phone" style="top:17px;">
      <svg width="24" height="24" viewBox="0 0 24 24"><path fill="#fff" d="M6.6 10.8a15.2 15.2 0 0 0 6.6 6.6l2.2-2.2a1 1 0 0 1 1-.25 11.4 11.4 0 0 0 3.6.57 1 1 0 0 1 1 1V20a1 1 0 0 1-1 1A17 17 0 0 1 3 4a1 1 0 0 1 1-1h3.5a1 1 0 0 1 1 1c0 1.25.2 2.45.57 3.57a1 1 0 0 1-.25 1z"/></svg>
      <span>604-555-0187</span>
    </div>
    <div class="contact contact--line" style="top:58px;">
      <svg width="13" height="10" viewBox="0 0 13 10"><rect width="13" height="10" fill="#fff"/><path d="M0 0l6.5 5L13 0" stroke="#6b3a80" stroke-width="1.3" fill="none"/></svg>
      <span>enviro@example.com</span>
    </div>
    <div class="contact contact--line" style="top:88px;">
      <svg width="13" height="13" viewBox="0 0 14 14"><circle cx="7" cy="7" r="6" fill="none" stroke="#fff" stroke-width="1.4"/><path d="M1 7h12M7 1c-3 3.5-3 8.5 0 12M7 1c3 3.5 3 8.5 0 12" stroke="#fff" stroke-width="1.2" fill="none"/></svg>
      <span>www.corvaneenvironmental.ca</span>
    </div>
  </div>
</section>

</body>
</html>
```